Postcard Design

We need a postcard design to attract new clients to use Larkfield Systems Group as their IT company. We are an IT support company offering a free 2 hour evaluation of the clients network. Also offering a 30 day free trial of our backup systems for all new clients. Looking for a post card to represent our company based on the company website, www.larkfieldsystems.example
Updates

Target Market(s)

Marketing small businesses with IT needs

Industry/Entity Type

It Company

Requirements
Must have
• The postcard needs to be two sided with an IT related picture on one side with the free evaluation offer and details of our services and 30 day free trial offer on the other side.

```html
<!DOCTYPE html>
<html lang="en">
<head>
<meta charset="utf-8">
<title>Larkfield Systems Group Postcard</title>
<link href="https://fonts.googleapis.com/css2?family=Ropa+Sans&family=Arimo&display=swap" rel="stylesheet">
<style>
  :root {
    --page: #e6e6e4;
    --blue-deep: #0d4a8c;
    --blue-mid: #1a66b0;
    --blue-light: #2f83cc;
    --yellow: #f7cd2a;
    --white: #ffffff;
    --ink-grey: #6b6b6b;
    --photo-dark: #1f2a24;
    --photo-mid: #55624f;
    --photo-light: #c9cdc4;
  }
  * { margin: 0; padding: 0; box-sizing: border-box; }
  html, body { width: 1200px; height: 1200px; overflow: hidden; }
  body {
    background: var(--page);
    position: relative;
    font-family: "Ropa Sans", sans-serif;
  }
  .card {
    position: absolute;
    width: 720px;
    height: 557px;
    background: var(--white);
    box-shadow: 0 2px 8px rgba(0,0,0,0.18);
    overflow: hidden;
  }
  /* ---------- back side ---------- */
  .card--back { left: 60px; top: 30px; }
  .info-panel {
    position: absolute; left: 0; top: 0;
    width: 348px; height: 460px;
    background: linear-gradient(160deg, var(--blue-light) 0%, var(--blue-mid) 45%, var(--blue-deep) 100%);
    color: var(--white);
    padding: 32px 24px 0 30px;
  }
  .company-name { font-size: 15px; letter-spacing: 0.2px; line-height: 1.5; text-transform: uppercase; }
  .contact { font-size: 14px; line-height: 1.62; }
  .divider { border: 0; border-top: 1px solid rgba(255,255,255,0.6); margin: 22px 0 22px; }
  .services-title { font-size: 21px; font-weight: 400; margin-bottom: 8px; }
  .services-list { list-style: none; font-size: 14px; }
  .services-list li { display: flex; align-items: center; height: 23px; }
  .services-list svg { width: 14px; height: 12px; margin-right: 11px; flex: none; }
  .mail-side { position: absolute; left: 348px; top: 0; right: 0; bottom: 0; font-family: "Arimo", sans-serif; color: var(--ink-grey); }
  .postage-area { position: absolute; right: 58px; top: 72px; font-size: 20px; text-align: center; line-height: 1.28; }
  .address-area { position: absolute; left: 116px; top: 230px; font-size: 20px; }
  .address-note { position: absolute; left: 37px; top: 282px; font-size: 14px; line-height: 1.3; }
  /* ---------- front side ---------- */
  .card--front { left: 420px; top: 613px; }
  .card-art { position: absolute; inset: 0; }
  .offer-headline {
    position: absolute; left: 31px; top: 24px;
    color: var(--white); font-size: 26px; line-height: 1.2; letter-spacing: 0.3px;
  }
  .brand-mark {
    position: absolute; right: 30px; top: 40px;
    display: flex; align-items: center; gap: 8px;
    color: var(--white); font-size: 15px; text-transform: uppercase; letter-spacing: 0.4px;
  }
  .brand-mark .mark-square { width: 14px; height: 14px; border: 2px solid var(--white); }
  .trial-badge {
    position: absolute; left: 13px; top: 370px;
    width: 176px; height: 176px; border-radius: 50%;
    background: rgba(26, 95, 170, 0.92);
    color: var(--white); text-align: center;
    display: flex; flex-direction: column; justify-content: center;
  }
  .trial-badge .trial-main { font-size: 26px; line-height: 1.05; letter-spacing: -0.3px; }
  .trial-badge .trial-sub { font-size: 14px; line-height: 1.45; margin-top: 8px; letter-spacing: 0.3px; }
</style>
</head>
<body>

<section class="card card--back" aria-label="Postcard back">
  <div class="info-panel">
    <p class="company-name">Larkfield Systems Group, LLC</p>
    <p class="contact">218 Harrow Lane, Brookvale, MO 63990<br>
      (555) 014-0237<br>
      info@larkfieldsystems.example<br>
      www.larkfieldsystems.example</p>
    <hr class="divider">
    <h2 class="services-title">OUR SERVICES</h2>
    <ul class="services-list">
      <li><svg viewBox="0 0 14 12"><path d="M1 6.5 L5 10.5 L13 1.5" fill="none" stroke="#fff" stroke-width="2.6"/></svg>Hardware Sales &amp; Support</li>
      <li><svg viewBox="0 0 14 12"><path d="M1 6.5 L5 10.5 L13 1.5" fill="none" stroke="#fff" stroke-width="2.6"/></svg>Local &amp; Remote Backup</li>
      <li><svg viewBox="0 0 14 12"><path d="M1 6.5 L5 10.5 L13 1.5" fill="none" stroke="#fff" stroke-width="2.6"/></svg>Security</li>
      <li><svg viewBox="0 0 14 12"><path d="M1 6.5 L5 10.5 L13 1.5" fill="none" stroke="#fff" stroke-width="2.6"/></svg>Data Recovery</li>
      <li><svg viewBox="0 0 14 12"><path d="M1 6.5 L5 10.5 L13 1.5" fill="none" stroke="#fff" stroke-width="2.6"/></svg>Internet &amp; Email</li>
      <li><svg viewBox="0 0 14 12"><path d="M1 6.5 L5 10.5 L13 1.5" fill="none" stroke="#fff" stroke-width="2.6"/></svg>Network Design &amp; Support</li>
      <li><svg viewBox="0 0 14 12"><path d="M1 6.5 L5 10.5 L13 1.5" fill="none" stroke="#fff" stroke-width="2.6"/></svg>Server Sales, Integration &amp; Support</li>
      <li><svg viewBox="0 0 14 12"><path d="M1 6.5 L5 10.5 L13 1.5" fill="none" stroke="#fff" stroke-width="2.6"/></svg>Software Sales &amp; Installation</li>
      <li><svg viewBox="0 0 14 12"><path d="M1 6.5 L5 10.5 L13 1.5" fill="none" stroke="#fff" stroke-width="2.6"/></svg>Website Design</li>
    </ul>
  </div>
  <div class="mail-side">
    <p class="postage-area">Postage<br>Area</p>
    <p class="address-area">Address Area</p>
    <p class="address-note">The only text allowed in the Address Area<br>
      is the recipient mailing address.<br>
      Red zones may have no text or<br>
      graphics darker than 7% grayscale.</p>
  </div>
</section>

<section class="card card--front" aria-label="Postcard front">
  <svg class="card-art" viewBox="0 0 720 557" preserveAspectRatio="none">
    <defs>
      <linearGradient id="photoTone" x1="0" y1="0" x2="1" y2="0.4">
        <stop offset="0" stop-color="var(--photo-light)"/>
        <stop offset="0.45" stop-color="var(--photo-mid)"/>
        <stop offset="1" stop-color="var(--photo-dark)"/>
      </linearGradient>
      <linearGradient id="bandTone" x1="0" y1="0" x2="1" y2="1">
        <stop offset="0" stop-color="var(--blue-mid)"/>
        <stop offset="1" stop-color="var(--blue-deep)"/>
      </linearGradient>
    </defs>
    <rect width="720" height="557" fill="url(#photoTone)" role="img" aria-label="Photo of network switches with patch cables and fibre leads in a server rack"/>
    <path d="M0 0 H720 V175 C560 120 300 98 0 118 Z" fill="var(--yellow)"/>
    <path d="M0 0 H720 V166 C560 108 300 86 0 98 Z" fill="url(#bandTone)"/>
  </svg>
  <h1 class="offer-headline">2 HOUR EVALUATION OF YOUR NETWORK<br>FOR FREE!!</h1>
  <div class="brand-mark"><span class="mark-square"></span>Larkfield Systems Group</div>
  <div class="trial-badge">
    <p class="trial-main">30 DAY<br>FREE TRIAL</p>
    <p class="trial-sub">OF OUR BACKUP<br>SYSTEMS FOR ALL<br>NEW CLIENTS</p>
  </div>
</section>

</body>
</html>
```